Business Card Design Project

We need a business card for a chiropractic and rehabilitation center. We already have a logo and need the card to follow the color and feel of the logo.

Target Market(s)

adults 30-55 that have some ache or pain that is interfering with their life, so much as they are ready to do something about it.

Industry/Entity Type

Business

```html
<!DOCTYPE html>
<html lang="en">
<head>
<meta charset="utf-8">
<title>VitalCore Care Business Card</title>
<link rel="stylesheet" href="https://fonts.googleapis.com/css2?family=Open+Sans:wght@400;600;700&display=swap">
<style>
  :root {
    --page-bg: #e9e6e1;
    --card-white: #fbfbf9;
    --brand-red: #b8172c;
    --brand-grey: #55575a;
    --brand-grey-dark: #3f4144;
    --brand-grey-light: #76787b;
    --rule-grey: #b9bbbd;
    --text-light: #ffffff;
    --text-muted: #e6e6e6;
  }
  * { margin: 0; padding: 0; box-sizing: border-box; }
  html, body {
    width: 1200px;
    height: 800px;
    overflow: hidden;
    background: var(--page-bg);
    font-family: "Open Sans", Arial, sans-serif;
  }
  .canvas {
    position: relative;
    width: 1200px;
    height: 800px;
  }
  .business-card {
    position: absolute;
    left: 100px;
    top: 114px;
    width: 1000px;
    height: 572px;
    background: var(--card-white);
    overflow: hidden;
    box-shadow: 0 6px 24px rgba(0,0,0,0.18);
  }
  .card-shapes {
    position: absolute;
    inset: 0;
  }
  .brand-name {
    position: absolute;
    left: 440px;
    top: 116px;
    font-size: 56px;
    font-weight: 600;
    line-height: 1;
    color: var(--brand-grey);
    white-space: nowrap;
  }
  .person {
    position: absolute;
    left: 44px;
    top: 378px;
    color: var(--text-light);
  }
  .person-name {
    font-size: 40px;
    font-weight: 700;
    line-height: 1.1;
  }
  .person-role {
    font-size: 24px;
    font-weight: 400;
    margin-top: 14px;
    color: var(--text-muted);
  }
  .contact-list {
    position: absolute;
    left: 470px;
    top: 268px;
    color: var(--text-light);
    font-size: 27px;
    line-height: 56px;
    list-style: none;
  }
  .contact-item {
    display: flex;
    white-space: nowrap;
  }
  .contact-label {
    width: 130px;
  }
  .contact-sep {
    width: 26px;
  }
</style>
</head>
<body>
<main class="canvas">
  <section class="business-card">
    <svg class="card-shapes" width="1000" height="572" viewBox="0 0 1000 572" aria-hidden="true">
      <defs>
        <linearGradient id="nameBandFade" x1="0" y1="0" x2="0" y2="1">
          <stop offset="0" stop-color="#76787b"/>
          <stop offset="1" stop-color="#3f4144"/>
        </linearGradient>
      </defs>
      <line x1="330" y1="214" x2="520" y2="214" stroke="#b9bbbd" stroke-width="3"/>
      <polygon points="430,240 1000,240 1000,572 300,572" fill="#b8172c"/>
      <polygon points="0,340 400,340 292,548 0,548" fill="url(#nameBandFade)"/>
    </svg>

    <p class="brand-name">VitalCore Care</p>

    <div class="person">
      <p class="person-name">Daniel Marsh</p>
      <p class="person-role">manager</p>
    </div>

    <ul class="contact-list">
      <li class="contact-item"><span class="contact-label">Office</span><span class="contact-sep">:</span><span class="contact-value">+0 555 210 4400</span></li>
      <li class="contact-item"><span class="contact-label">Cell</span><span class="contact-sep">:</span><span class="contact-value">+0 555 210 4411</span></li>
      <li class="contact-item"><span class="contact-label">E-mail</span><span class="contact-sep">:</span><span class="contact-value">daniel@vitalcorecare.com</span></li>
      <li class="contact-item"><span class="contact-label">Website</span><span class="contact-sep">:</span><span class="contact-value">www.vitalcorecare.com</span></li>
    </ul>
  </section>
</main>
</body>
</html>
```